Business Card Design Project

Recently had a new logo made up for my company and new business cards done as well. I have attached the logos for your viewing. Additional projects may be needed. Good luck!

Business

```html
<!DOCTYPE html>
<html lang="en">
<head>
<meta charset="utf-8">
<title>Corran Financial Group – Business Cards</title>
<link rel="stylesheet" href="https://fonts.googleapis.com/css2?family=Cinzel:wght@600&family=Oswald:wght@400;500&family=Pathway+Gothic+One&display=swap">
<style>
  :root {
    --backdrop: #e9e6e1;
    --navy: #262a3b;
    --gold: #c9ad76;
    --white: #f4f4f2;
  }
  * { box-sizing: border-box; margin: 0; padding: 0; }
  html, body { width: 1200px; height: 900px; overflow: hidden; }
  body {
    background: var(--backdrop);
    position: relative;
    font-family: "Pathway Gothic One", "Arial Narrow", sans-serif;
  }
  .card {
    position: absolute;
    width: 640px;
    height: 366px;
    background: var(--navy);
    border-radius: 4px;
    overflow: hidden;
  }
  .card--back { left: 440px; top: 50px; }
  .card--front { left: 120px; top: 470px; }

  /* back side */
  .back-mark {
    position: absolute;
    inset: 0;
    display: flex;
    align-items: center;
    justify-content: center;
    gap: 22px;
  }
  .back-mark__square {
    width: 70px; height: 70px;
    border: 6px solid var(--gold);
  }
  .back-mark__name {
    font-family: "Cinzel", Georgia, serif;
    font-weight: 600;
    font-size: 58px;
    letter-spacing: 6px;
    color: var(--gold);
  }

  /* front side */
  .brand {
    position: absolute;
    left: 26px; top: 24px;
    right: 26px;
    display: flex;
    align-items: center;
    gap: 14px;
  }
  .brand__square {
    flex: none;
    width: 60px; height: 60px;
    border: 5px solid var(--gold);
  }
  .brand__name {
    font-family: "Cinzel", Georgia, serif;
    font-weight: 600;
    font-size: 27px;
    letter-spacing: 3px;
    color: var(--gold);
    white-space: nowrap;
  }
  .person {
    position: absolute;
    left: 60px; top: 140px;
    color: var(--white);
  }
  .person__name {
    font-family: "Oswald", "Arial Narrow", sans-serif;
    font-weight: 500;
    font-size: 22px;
    letter-spacing: 3px;
  }
  .person__role {
    font-size: 17px;
    letter-spacing: 1px;
    margin-top: 2px;
  }
  .contact {
    position: absolute;
    left: 40px; bottom: 34px;
    display: grid;
    grid-template-columns: 64px auto;
    row-gap: 4px;
    font-size: 18px;
    letter-spacing: 1px;
  }
  .contact__label { color: var(--gold); text-align: right; padding-right: 22px; }
  .contact__value { color: var(--white); }
  .address {
    position: absolute;
    left: 360px; bottom: 34px;
    color: var(--white);
    font-size: 18px;
    line-height: 26px;
    letter-spacing: 1px;
  }
</style>
</head>
<body>
  <section class="card card--back" aria-label="Business card, back">
    <div class="back-mark">
      <div class="back-mark__square"></div>
      <div class="back-mark__name">CORRAN</div>
    </div>
  </section>

  <section class="card card--front" aria-label="Business card, front">
    <div class="brand">
      <div class="brand__square"></div>
      <div class="brand__name">CORRAN FINANCIAL GROUP</div>
    </div>

    <div class="person">
      <div class="person__name">DANIEL R. CORRAN</div>
      <div class="person__role">Estate Planning and Insurance Specialist</div>
    </div>

    <div class="contact">
      <span class="contact__label">tel</span><span class="contact__value">555-014-2287</span>
      <span class="contact__label">fax</span><span class="contact__value">555-014-6130</span>
      <span class="contact__label">email</span><span class="contact__value">dcorran@corranfinancial.com</span>
    </div>

    <div class="address">
      4120 Halden Parkway, Suite 310E<br>
      Brookvale, New York 10987<br>
      www.corranfinancial.com
    </div>
  </section>
</body>
</html>
```